Nanny Share Ecommerce Website for Finding Childcare and Parents who need Childcare HuggaSitter.com

Our company needs an ecommerce website (HuggaSitter.com) for a US subscription based service strictly for nanny sharing that connects families and caregivers. The website would allow families to connect with one another as well as to search for nannies. The service would be searchable for other families by location (by radius or zip code), children demographic (age range/gender/special needs), days of week or times, after school care, school closure days (holidays), etc. The service would also be searchable for nannies based on gender, provider age range, years experience, language, hourly rate, transportation available, certification (CPR first aid), education etc. The search fields would be searchable and sortable and allow to connect with the provider (after paying subscription fee). The service would be similar to tendly.com in that it would allow for families and caregivers to post photos as well as a short bio of the themselves. There would also be a feedback/star rating mechanism to rate caregivers who have performed work for families (viewable to public). The service would be free for nannies to post their bios and only a subscription based service for families to connect with other families or with caregivers (able to view bio but need service to connect). There will be a short bio on the benefits of nanny sharing (reduced cost, increased flexibility for parents, reduced illness, increased socialization with other children vs. sole nanny), as well as Q&A section with best practices.

Target Market(s)

Families, Nannies

Industry/Entity Type

Childcare

Logo Text

Hugga Sitter

Coding

Coded - Design and coding required

Number of Pages Required

5+ page

Requirements
Must have
• Searchable (need to be able to search for families as well as nannies), responsive, functional, easy to use, add value to families and nannies. Needs to be able to collect payment for subscription.
Nice to have
• Optimized for mobile, SEO optimized

```html
<!DOCTYPE html>
<html lang="en">
<head>
<meta charset="utf-8">
<title>HuggaSitter.com – Nanny Share for Families and Caregivers</title>
<link rel="stylesheet" href="https://fonts.googleapis.com/css2?family=Open+Sans:ital,wght@0,300;0,400;0,600;0,700;1,700&family=Lobster&display=swap">
<style>
:root{
  --orange:#f26a2e;
  --orange-dark:#e0531c;
  --orange-soft:#f8a35c;
  --blue:#26b4d9;
  --teal:#2aa6b8;
  --teal-soft:rgba(42,166,184,.88);
  --pink:#f47fb5;
  --ink:#333a40;
  --grey:#7b8187;
  --rule:#e6e6e6;
  --faq:#6596ae;
  --footer:#1c1c1c;
  --white:#fff;
  --text:'Open Sans',sans-serif;
  --script:'Lobster',cursive;
}
*{box-sizing:border-box;margin:0;padding:0}
html,body{width:1200px;height:5042px;overflow:hidden}
body{font-family:var(--text);color:var(--ink);background:var(--white);font-size:13px;line-height:1.6}
.wrap{width:1080px;margin:0 auto;position:relative}
.photo{display:block}
p{color:var(--grey)}

/* header */
.site-header{height:100px;background:var(--white);position:relative;z-index:2}
.site-header .wrap{display:flex;align-items:center;justify-content:space-between;height:100px}
.brand{display:flex;align-items:center;gap:10px;font-size:26px;font-weight:700;color:var(--orange)}
.brand-dot{width:36px;height:36px;border-radius:50%;background:var(--pink)}
.main-nav{display:flex;gap:20px;font-size:14px}
.main-nav a{color:var(--ink);text-decoration:none}

/* hero */
.hero{height:570px;position:relative;background:linear-gradient(100deg,#fff4ea 0%,#ffe3cc 45%,#f9c39d 100%);overflow:hidden}
.hero-photo{position:absolute;right:0;top:0;width:660px;height:570px;background:radial-gradient(circle at 60% 45%,#f2a57e 0%,#e98862 35%,#f7d1b4 75%,rgba(255,230,210,0) 100%)}
.hero-copy{position:absolute;left:80px;top:170px;width:520px}
.hero-title{font-family:var(--text);font-style:italic;font-weight:700;color:var(--orange);line-height:1.15}
.hero-title .small{display:block;font-size:26px}
.hero-title .big{display:block;font-size:42px}
.hero-copy p{margin-top:16px;font-size:13px;color:#6a5f58;width:460px}
.hero-actions{display:flex;gap:14px;margin-top:28px}
.btn-pill{display:inline-block;border-radius:22px;padding:9px 24px;color:var(--white);font-size:12px;line-height:1.25;text-decoration:none;text-align:center}
.btn-pill b{display:block;font-size:14px;font-style:italic}
.btn-blue{background:var(--blue)}
.btn-orange{background:var(--orange)}

/* section titles */
.sec-title{text-align:center}
.sec-title .script{display:block;font-family:var(--script);color:var(--orange);font-size:28px;line-height:1}
.sec-title .main{display:block;font-size:32px;font-weight:300;color:var(--ink);line-height:1.2}

/* how it works */
.how{height:540px;padding-top:40px}
.steps{display:flex;justify-content:space-between;margin-top:60px}
.step{width:240px;text-align:center}
.step-icon{width:104px;height:104px;border-radius:50%;margin:0 auto 26px;display:flex;align-items:center;justify-content:center;border:2px solid var(--rule);border-top-color:var(--orange);border-right-color:var(--orange)}
.step h3{font-size:15px;font-weight:600;color:var(--ink);margin-bottom:6px}
.step p{font-size:12px}
.btn-center{display:block;width:170px;margin:50px auto 0;text-align:center;background:var(--blue);color:var(--white);border-radius:20px;padding:9px 0;font-size:13px;font-weight:700;text-decoration:none}

/* band with scalloped edge */
.band{position:relative;height:140px;background:var(--orange);padding-top:34px}
.band::after{content:"";position:absolute;left:0;right:0;bottom:-12px;height:24px;background:radial-gradient(circle at 12px 0,var(--orange) 11px,transparent 12px) repeat-x;background-size:24px 24px}
.band .sec-title .script,.band .sec-title .main{color:var(--white)}

/* services */
.services{height:800px;padding-top:70px}
.service-row{display:flex;align-items:center;justify-content:space-between;height:330px}
.service-row + .service-row{margin-top:40px}
.service-photo{width:500px;height:300px;border-radius:2px}
.service-photo.one{background:linear-gradient(135deg,#cbb7a6,#f1e4d6 55%,#b9a08c)}
.service-photo.two{background:linear-gradient(135deg,#d9c2b6,#f3ece3 50%,#8fbcc0)}
.service-text{width:520px}
.service-text h3{font-size:22px;font-weight:400;color:var(--ink);margin-bottom:14px}
.service-text p{font-size:12.5px}
.btn-small{display:inline-block;margin-top:22px;background:var(--blue);color:var(--white);border-radius:18px;padding:7px 30px;font-size:12px;font-weight:700;text-decoration:none}

/* benefits */
.benefits{height:710px;position:relative;overflow:hidden}
.benefits-bg{position:absolute;inset:0;background:linear-gradient(160deg,#3f5a1f 0%,#7d8d2a 30%,#d6c25a 55%,#9a6b33 80%,#4b3a1d 100%)}
.benefits .sec-title{position:relative;padding-top:48px}
.benefits .sec-title .main{color:var(--white)}
.bubble{position:absolute;width:200px;height:200px;border-radius:50%;background:var(--teal-soft);color:var(--white);text-align:center;padding:46px 26px 0}
.bubble svg{display:block;margin:0 auto 4px}
.bubble h4{font-size:15px;font-weight:400;line-height:1.25}
.bubble p{color:#e8f7fa;font-size:11px;line-height:1.4;margin-top:4px}
.bubble .more{color:var(--white);font-size:11px;font-weight:700}

/* find */
.find{height:540px;background:var(--pink);padding-top:44px}
.find .sec-title .script{color:var(--white)}
.find .sec-title .main{color:var(--white)}
.cards{display:flex;justify-content:center;gap:50px;margin-top:40px}
.card{width:262px;height:330px;background:var(--white);text-align:center;padding-top:28px}
.avatar{width:110px;height:110px;border-radius:50%;margin:0 auto 12px;border:4px solid #f3f3f3}
.avatar.a{background:#d9a78a}.avatar.b{background:#c99a72}.avatar.c{background:#b8836a}
.card h3{font-size:20px;font-weight:400;color:var(--teal);line-height:1.2}
.card .city{font-size:12px;color:var(--grey)}
.card .reviews{font-size:11px;color:var(--ink);display:flex;justify-content:center;gap:8px;align-items:center;margin:4px 0 10px}
.stars{color:#f5b53f;letter-spacing:1px}
.card p{font-size:11px;line-height:1.45;width:190px;margin:0 auto}
.card .more{display:block;margin-top:6px;font-size:11px;color:var(--blue);font-weight:700}

/* testimonials */
.testimonials{height:330px;padding-top:46px;position:relative}
.quotes{display:flex;justify-content:center;gap:60px;margin-top:36px;align-items:center}
.arrow{position:absolute;top:200px;color:var(--grey);font-size:26px}
.arrow.left{left:78px}.arrow.right{right:78px}
.quote{display:flex;gap:18px;width:440px;align-items:center}
.q-photo{flex:0 0 130px;height:130px;border-radius:50%;border:4px solid var(--orange)}
.q-photo.a{background:#e3b99b}.q-photo.b{background:#d6a98c}
.quote blockquote{font-size:12px;color:var(--grey)}
.quote .mark{font-family:Georgia,serif;color:var(--orange);font-size:28px;line-height:0;vertical-align:-8px;margin-right:4px}
.quote cite{display:block;margin-top:8px;font-style:normal;color:var(--orange);font-size:12px}

/* faq */
.faq{height:910px;position:relative;background:var(--faq);padding-top:56px;overflow:hidden}
.faq::before{content:"";position:absolute;left:0;right:0;top:-12px;height:24px;background:radial-gradient(circle at 12px 24px,var(--faq) 11px,transparent 12px) repeat-x;background-size:24px 24px}
.faq-photo{position:absolute;right:0;top:0;width:620px;height:910px;background:linear-gradient(90deg,rgba(101,150,174,0) 0%,rgba(180,205,218,.55) 50%,rgba(210,225,232,.6) 100%)}
.faq .sec-title{position:relative}
.faq .sec-title .script{color:var(--white)}
.faq .sec-title .main{color:var(--white)}
.faq-list{position:relative;margin-top:40px}
.faq-item{display:flex;gap:16px;margin-bottom:26px}
.faq-num{flex:0 0 34px;height:34px;border-radius:50%;background:var(--white);color:var(--faq);font-weight:700;font-size:16px;display:flex;align-items:center;justify-content:center}
.faq-item h3{font-size:17px;font-weight:400;color:#1f2e38;margin:4px 0 8px}
.faq-item p{color:#eef5f8;font-size:11.5px;line-height:1.55;width:1000px}

/* footer */
.site-footer{height:370px;background:var(--footer);padding-top:50px}
.foot-cols{display:flex;justify-content:space-between}
.foot-col h4{color:var(--orange);font-size:14px;font-weight:600;margin-bottom:8px}
.foot-col ul{list-style:none}
.foot-col li{color:#cfcfcf;font-size:12px;line-height:1.6}
.copyright{height:32px;background:#111;color:#8a8a8a;font-size:11px;text-align:center;line-height:32px}
</style>
</head>
<body>

<header class="site-header">
  <div class="wrap">
    <div class="brand"><span class="brand-dot"></span>HuggaSitter.com</div>
    <nav class="main-nav">
      <a href="#">Home</a><a href="#">About</a><a href="#">How It Works</a><a href="#">Our Services</a><a href="#">Our Benefits</a><a href="#">FAQ</a><a href="#">Contact</a>
    </nav>
  </div>
</header>

<section class="hero">
  <div class="hero-photo photo" role="img" aria-label="Photo of a smiling mother carrying a happy child pretending to fly"></div>
  <div class="hero-copy">
    <h1 class="hero-title"><span class="small">Quality &amp; Professional Child Care</span><span class="big">At An Affordable Price</span></h1>
    <p>Lorem ipsum dolor sit amet, consectetur adipiscing elit. Curabitur consequat vulputate urna. Sed vitae tortor eu nisl tempus dictum. Vivamus malesuada tristique iaculis.</p>
    <div class="hero-actions">
      <a class="btn-pill btn-blue" href="#">Are You a Parent?<b>Find Nannies</b></a>
      <a class="btn-pill btn-orange" href="#">Are You a Nanny?<b>Find Jobs</b></a>
    </div>
  </div>
</section>

<section class="how">
  <div class="wrap">
    <h2 class="sec-title"><span class="script">How</span><span class="main">It Works</span></h2>
    <div class="steps">
      <div class="step">
        <div class="step-icon"><svg width="50" height="50" viewBox="0 0 50 50"><circle cx="25" cy="17" r="9" fill="#f26a2e"/><path d="M8 44c2-11 9-16 17-16s15 5 17 16z" fill="#26b4d9"/></svg></div>
        <h3>Create a Profile For Free</h3>
        <p>Lorem ipsum dolor sit amet, consectetur adipiscing elit. In gravida feugiat ex vel. Etiam malesuada.</p>
      </div>
      <div class="step">
        <div class="step-icon"><svg width="50" height="50" viewBox="0 0 50 50"><circle cx="21" cy="21" r="12" fill="none" stroke="#f26a2e" stroke-width="4"/><path d="M30 30l12 12" stroke="#26b4d9" stroke-width="5" stroke-linecap="round"/></svg></div>
        <h3>Free Search for Families/Nannies</h3>
        <p>Lorem ipsum dolor sit amet, consectetur adipiscing elit. In gravida feugiat ex vel. Etiam malesuada.</p>
      </div>
      <div class="step">
        <div class="step-icon"><svg width="50" height="50" viewBox="0 0 50 50"><rect x="6" y="12" width="38" height="26" rx="4" fill="#26b4d9"/><path d="M6 16l19 12 19-12" fill="none" stroke="#fff" stroke-width="3"/><circle cx="40" cy="12" r="6" fill="#f26a2e"/></svg></div>
        <h3>Contact Families &amp; Caregivers</h3>
        <p>Lorem ipsum dolor sit amet, consectetur adipiscing elit. In gravida feugiat ex vel. Etiam malesuada.</p>
      </div>
      <div class="step">
        <div class="step-icon"><svg width="50" height="50" viewBox="0 0 50 50"><path d="M8 14h6l4 16h22l4-12H17" fill="none" stroke="#26b4d9" stroke-width="3.5" stroke-linejoin="round"/><circle cx="20" cy="38" r="4" fill="#f26a2e"/><circle cx="38" cy="38" r="4" fill="#f26a2e"/></svg></div>
        <h3>Enjoy Your Personalized Childcare</h3>
        <p>Lorem ipsum dolor sit amet, consectetur adipiscing elit. In gravida feugiat ex vel. Etiam malesuada.</p>
      </div>
    </div>
    <a class="btn-center" href="#">Register Now</a>
  </div>
</section>

<section class="band">
  <h2 class="sec-title"><span class="script">Our</span><span class="main">Services</span></h2>
</section>

<section class="services">
  <div class="wrap">
    <div class="service-row">
      <div class="service-photo one photo" role="img" aria-label="Photo of parents relaxing on a sofa with their baby"></div>
      <div class="service-text">
        <h3>Matching Families</h3>
        <p>We know that finding a family to share your caregiver is just as important as finding a nanny. That's why we specialize in helping you find local families that are looking for the same personalized care. You'll have the ability to search for families by the age range of children, gender, location, days or times of the week, as well as other personalized preferences for that perfect family.</p>
        <a class="btn-small" href="#">Get Started</a>
      </div>
    </div>
    <div class="service-row">
      <div class="service-text">
        <h3>Finding Caregivers</h3>
        <p>Once you've found the perfect families to share your caregiver we recommend you start your search for a nanny that meets your personalized needs. Search for the perfect caregiver by education and experience, location, rates, certifications, and other qualifications. We'll ensure that you and the families you partner with find the perfect caregiver to complement your personalized care needs.</p>
        <a class="btn-small" href="#">Get Started</a>
      </div>
      <div class="service-photo two photo" role="img" aria-label="Photo of a caregiver reading with children in a play tent"></div>
    </div>
  </div>
</section>

<section class="benefits">
  <div class="benefits-bg photo" role="img" aria-label="Photo of a child playing among blossoming trees in sunlight"></div>
  <h2 class="sec-title"><span class="script">Our</span><span class="main">Benefits</span></h2>
  <div class="bubble" style="left:150px;top:150px">
    <svg width="26" height="22" viewBox="0 0 26 22"><rect x="2" y="4" width="22" height="15" rx="2" fill="none" stroke="#fff" stroke-width="2"/><circle cx="13" cy="11.5" r="3" fill="#fff"/></svg>
    <h4>Reduced Cost</h4>
    <p>We know that paying for childcare is expensive so share it.</p>
    <span class="more">Read More</span>
  </div>
  <div class="bubble" style="left:500px;top:200px">
    <svg width="24" height="24" viewBox="0 0 24 24"><circle cx="12" cy="12" r="9" fill="none" stroke="#fff" stroke-width="2"/><path d="M12 6v6l4 3" stroke="#fff" stroke-width="2" fill="none"/></svg>
    <h4>Increased Flexibility for Parents</h4>
    <p>Share the care. Do you work weekends, evenings?</p>
    <span class="more">Read More</span>
  </div>
  <div class="bubble" style="left:850px;top:150px">
    <svg width="24" height="22" viewBox="0 0 24 22"><path d="M12 20S2 13 2 7a5 5 0 0 1 10-1 5 5 0 0 1 10 1c0 6-10 13-10 13z" fill="#fff"/></svg>
    <h4>Reduced Illness</h4>
    <p>Did you know that daycare is an increased risk factor?</p>
    <span class="more">Read More</span>
  </div>
  <div class="bubble" style="left:300px;top:400px">
    <svg width="28" height="22" viewBox="0 0 28 22"><circle cx="9" cy="7" r="4" fill="#fff"/><circle cx="19" cy="7" r="4" fill="#fff"/><path d="M2 20c1-6 4-8 7-8s6 2 7 8zM12 20c1-6 4-8 7-8s6 2 7 8z" fill="#fff"/></svg>
    <h4>Increased Socialization</h4>
    <p>Social development is key in the early years of child.</p>
    <span class="more">Read More</span>
  </div>
  <div class="bubble" style="left:700px;top:420px">
    <svg width="24" height="22" viewBox="0 0 24 22"><path d="M12 2l3 6 7 1-5 5 1 7-6-3-6 3 1-7-5-5 7-1z" fill="#fff"/></svg>
    <h4>We Are More Than Just a Nanny Agency</h4>
    <p>We are always in the loop to match you well.</p>
    <span class="more">Read More</span>
  </div>
</section>

<section class="find">
  <h2 class="sec-title"><span class="script">Find</span><span class="main">The Perfect Babysitter or Nanny for You</span></h2>
  <div class="cards">
    <article class="card">
      <div class="avatar a photo" role="img" aria-label="Profile photo of nanny Rosie"></div>
      <h3>Rosie</h3>
      <div class="city">San Francisco</div>
      <div class="reviews"><span>264 Reviews</span><span class="stars">★★★★★</span></div>
      <p>Morbi eu lectus in urna finibus hendrerit id quis dui. Suspendisse volutpat massa ipsum, non interdum justo placerat at.</p>
      <span class="more">Read More</span>
    </article>
    <article class="card">
      <div class="avatar b photo" role="img" aria-label="Profile photo of nanny Lena"></div>
      <h3>Lena</h3>
      <div class="city">San Francisco</div>
      <div class="reviews"><span>122 Reviews</span><span class="stars">★★★★★</span></div>
      <p>Morbi eu lectus in urna finibus hendrerit id quis dui. Suspendisse volutpat massa ipsum, non interdum justo placerat at.</p>
      <span class="more">Read More</span>
    </article>
    <article class="card">
      <div class="avatar c photo" role="img" aria-label="Profile photo of nanny Tessa"></div>
      <h3>Tessa</h3>
      <div class="city">San Francisco</div>
      <div class="reviews"><span>325 Reviews</span><span class="stars">★★★★★</span></div>
      <p>Morbi eu lectus in urna finibus hendrerit id quis dui. Suspendisse volutpat massa ipsum, non interdum justo placerat at.</p>
      <span class="more">Read More</span>
    </article>
  </div>
</section>

<section class="testimonials">
  <h2 class="sec-title"><span class="script">What</span><span class="main">Our Parents Are Saying</span></h2>
  <span class="arrow left">&#8249;</span><span class="arrow right">&#8250;</span>
  <div class="quotes">
    <div class="quote">
      <div class="q-photo a photo" role="img" aria-label="Portrait of parent Dana Brooks"></div>
      <blockquote><span class="mark">&ldquo;</span>Sed posuere dictum dapibus. Fusce vel nisi purus. Laoreet posuere dolor, ac auctor arcu sollicitudin quis.<cite>– Dana Brooks</cite></blockquote>
    </div>
    <div class="quote">
      <div class="q-photo b photo" role="img" aria-label="Portrait of parent Priya Lane"></div>
      <blockquote><span class="mark">&ldquo;</span>Sed posuere dictum dapibus. Fusce vel nisi purus. Laoreet posuere dolor, ac auctor arcu sollicitudin quis.<cite>– Priya Lane</cite></blockquote>
    </div>
  </div>
</section>

<section class="faq">
  <div class="faq-photo photo" role="img" aria-label="Faded photo of a mother holding her child"></div>
  <div class="wrap">
    <h2 class="sec-title"><span class="script">Frequently</span><span class="main">Asked Questions</span></h2>
    <div class="faq-list">
      <div class="faq-item"><span class="faq-num">?</span><div>
        <h3>What is Nanny Sharing?</h3>
        <p>Nanny share is typically when two or more families employ one nanny, sharing the cost of his or her salary. Most nannies watch the children together and many families work together to personalize schedules. Since both families are contributing to the nanny's pay, the nanny is usually able to earn more than working for a single family while also being a cost effective solution for the parents.</p>
      </div></div>
      <div class="faq-item"><span class="faq-num">?</span><div>
        <h3>Do I search for a Nanny or Family First?</h3>
        <p>We recommend matching with a family with similar personalized needs for care and discussing as a group what the specific duties or requirements for employment will be for the nanny.</p>
      </div></div>
      <div class="faq-item"><span class="faq-num">?</span><div>
        <h3>How do we determine the nanny's salary and benefits?</h3>
        <p>We recommend that all parties of the nanny share including families and nannies partake the in the benefits. Remember that the nanny will have increased responsibility while caring for more children. We recommend structuring pay in a way that compensates the nanny for her increased responsibility as well as any other benefits (paid time off, sick time, overtime etc). The more the nanny compensation grows, the lower your cost stays. Note that most nanny share contracts will have multiple rates depending on if the nanny is watching for more than one family or if a child is sick and not present.</p>
      </div></div>
      <div class="faq-item"><span class="faq-num">?</span><div>
        <h3>Do we need to withhold employment tax for the nanny share?</h3>
        <p>According to the Federal Revenue Office Household Employer's Tax Guide, if you pay more than $2,000 annually or $1,000 a quarter to a person working in your home you need to pay employment taxes. This requires a family to withhold Social Security and Medicare and to pay a matching portion. State and federal unemployment insurance taxes may also be due. There are two components of the "nanny tax." The employee nanny's withholding taxes and the employer contribution (families). Typically, you'd withhold Social Security and Medicare taxes and you may also withhold federal, state, and maybe city income taxes from your employee's pay. As an employer, you'd pay a matching portion of Social Security and Medicare as well as federal and state unemployment insurance taxes. States differ in their requirements; some don't have income taxes while other states require additional taxes withheld. We have partnered with a trusted payroll provider to help to provide easy-to-manage tax and payroll services at a discount.</p>
      </div></div>
    </div>
  </div>
</section>

<footer class="site-footer">
  <div class="wrap foot-cols">
    <div class="foot-col"><h4>Discover</h4><ul><li>Parents: How It Works</li><li>Sitters: How It Works</li><li>Gift Cards</li><li>Childcare Resources</li><li>Get the App</li><li>Find Schools and Groups</li><li>Pricing</li><li>Support</li></ul></div>
    <div class="foot-col"><h4>Company</h4><ul><li>About Us</li><li>Press</li><li>Corporate Benefits</li><li>Careers at HuggaSitter</li><li>Affiliate Program</li><li>Babysitting Jobs</li><li>Nanny Jobs</li><li>Terms of Service</li><li>Privacy Policy</li></ul></div>
    <div class="foot-col"><h4>Nannies near me</h4><ul><li>San Francisco Nannies</li><li>New York City Nannies</li><li>Chicago Nannies</li><li>Los Angeles Nannies</li><li>Seattle Nannies</li><li>Portland Nannies</li><li>Washington DC Nannies</li><li>Boston Nannies</li><li>Denver Nannies</li><li>San Diego Nannies</li><li>See all cities</li></ul></div>
    <div class="foot-col"><h4>Programs/Resources</h4><ul><li>Community</li><li>Child Care Articles &amp; Resources</li><li>Pet Care Articles &amp; Resources</li><li>Senior Care Articles &amp; Resources</li><li>House &amp; Home Articles and Resources</li><li>Ask a Question</li><li>Post a Story</li><li>Explore Topics</li><li>How-to Guides</li><li>Research &amp; Data</li></ul></div>
    <div class="foot-col"><h4>Follow HuggaSitter</h4><ul><li>Friendbook</li><li>Snapgram</li><li>Chirper</li><li>Circles+</li><li>Childcare Blog</li><li>Pinboardly</li><li>ViewTube</li></ul></div>
  </div>
</footer>
<div class="copyright">Copyright 2016 HuggaSitter.com. All Rights Reserved.</div>

</body>
</html>
```